Driving-coach/trainer who wants to inform about the offer and how I can help people to drive more re

I need a flyer that informs potential customers about my offer.

DL size 210 mm x 99 mm, vertical!

I'm a trainer/coach who helps people to drive a car more relaxed, without fear and more confident.

It's a one to one training. I do train people in their own car. It gets people their freedom back to go where and when they like to go by own car...
Updates

Project Deadline Extended Reason: I would like to extend my project... didn't find the time to give feedback because of unexpected other jobs I had to do.Would be great if you could extend my project around 5 more days. THANKS. Added Wednesday, January 4, 2017

Target Market(s)

People (man an woman) who are afraid of driving a car, or are very stressed while driving....

Industry/Entity Type

Life Coaching

Font styles to use
Sans Serif

Colors
acd136

Requirements
Must have
• Page 1:
• -my offer (see text-pdf)
• -three fotos (see attached files "Pixavine") of people who are satisfied with my offer
• Page 2:
• -advantages in the work with me.
• -contact information
• -and a picture of me (see attached file) next to the contact information or the advantages of my work
• -my logo (see attached file) on Page 1 + 2
• -i like a "clear" and structured layout. "Less is more"

```html
<!DOCTYPE html>
<html lang="de">
<head>
<meta charset="utf-8">
<title>Fahrangst erfolgreich überwinden – Flyer</title>
<link href="https://fonts.googleapis.com/css2?family=Bebas+Neue&family=Open+Sans:wght@400;600;700&family=Lato:wght@400&display=swap" rel="stylesheet">
<style>
  :root{
    --green:#acd136;
    --green-dark:#95b82a;
    --grey-text:#6d6e70;
    --dark-text:#3f4042;
    --panel:#f0f0f0;
    --paper:#ffffff;
    --backdrop:#e4e4e2;
    --photo-a:#c9cfc4;
    --photo-b:#8d9393;
  }
  *{box-sizing:border-box;margin:0;padding:0}
  html,body{width:1125px;height:1200px;overflow:hidden}
  body{background:var(--backdrop);font-family:"Open Sans",Arial,sans-serif;position:relative}
  .flyer{position:absolute;width:394px;height:828px;background:var(--paper);box-shadow:0 3px 10px rgba(0,0,0,.25);overflow:hidden}
  .flyer--front{left:85px;top:110px}
  .flyer--back{left:545px;top:170px}
  .flyer__title{position:absolute;top:18px;left:0;width:100%;text-align:center;font-weight:700;font-size:18.5px;color:var(--grey-text);letter-spacing:.2px}
  .flyer__title em{font-style:normal;color:var(--green)}
  .flyer__bg{position:absolute;left:0;top:0}
  .hero-photo{position:absolute;left:0;width:394px}
  .badge{position:absolute;width:112px;height:112px;border-radius:50%;background:var(--green);border:4px solid #fff;box-shadow:0 2px 6px rgba(0,0,0,.3);display:flex;align-items:center;justify-content:center;text-align:center;color:#fff;font-size:15px;line-height:1.25}
  .bebas{font-family:"Bebas Neue",Impact,sans-serif;font-weight:400}
  .headline{position:absolute;color:var(--green);text-align:center}
  .wish-list{position:absolute;list-style:none;font-size:13.5px;color:var(--dark-text)}
  .wish-list li{display:flex;align-items:center;gap:10px;height:22px}
  .tick-dot{width:12px;height:12px;border-radius:50%;background:var(--green);display:inline-flex;align-items:center;justify-content:center;flex:none}
  .pill{position:absolute;background:var(--green);color:#fff;border-radius:9px;display:flex;align-items:center;justify-content:center;box-shadow:0 2px 4px rgba(0,0,0,.25)}
  .detail-list{position:absolute;list-style:none;font-size:8.4px;line-height:1.3;color:var(--dark-text);text-align:justify}
  .detail-list li{position:relative;padding-left:14px;margin-bottom:6px}
  .detail-list li::before{content:"";position:absolute;left:1px;top:2px;width:6px;height:3px;border-left:1.5px solid var(--green);border-bottom:1.5px solid var(--green);transform:rotate(-45deg)}
  .detail-list .hl{color:var(--green)}
  .contact{position:absolute;left:16px;color:var(--green);font-weight:700}
  .contact__phone{font-size:14px;display:flex;align-items:center;gap:7px}
  .contact__web{font-size:11px;margin-top:3px}
  .step{position:absolute;top:309px;width:82px;height:82px;border-radius:50%;background:var(--green);border:3px solid #fff;box-shadow:0 1px 4px rgba(0,0,0,.25);color:#fff;text-align:center;display:flex;flex-direction:column;align-items:center;padding-top:10px}
  .step__num{font-size:25px;line-height:1}
  .step__text{font-size:7px;line-height:1.15;margin-top:8px;padding:0 6px}
  .quote{position:absolute;left:14px;top:618px;font-family:"Lato",Arial,sans-serif;font-size:11.5px;color:var(--dark-text);line-height:1.45}
  .quote__mark{color:var(--green);font-size:22px;font-family:Georgia,serif}
  .coach-name{position:absolute;left:14px;top:672px;font-family:"Lato",Arial,sans-serif;color:var(--green-dark);font-size:14.5px;letter-spacing:.8px;line-height:1.2}
  .coach-name small{display:block;font-size:11.5px;letter-spacing:.5px}
  .coach-photo{position:absolute;left:228px;top:598px;width:150px;height:200px;border-radius:70px 70px 10px 10px;background:linear-gradient(180deg,#d8cfc6 0%,#f4f4f4 55%,#e6e6e6 100%)}
</style>
</head>
<body>

<!-- Page 1 -->
<section class="flyer flyer--front">
  <svg class="flyer__bg" width="394" height="828" viewBox="0 0 394 828" aria-hidden="true">
    <rect x="0" y="280" width="394" height="470" fill="var(--panel)"/>
    <path d="M0 720 C110 680 230 760 394 740 L394 828 L0 828 Z" fill="#fff"/>
    <path d="M0 740 C90 700 180 720 270 780 C320 805 360 800 394 770 L394 790 C350 818 300 815 250 790 C170 745 90 725 0 755 Z" fill="var(--green)"/>
    <path d="M0 84 C120 50 270 50 394 75 L394 62 C270 40 120 42 0 74 Z" fill="var(--green)"/>
    <path d="M0 350 C120 330 240 300 394 245 L394 262 C250 320 120 350 0 365 Z" fill="var(--green)"/>
  </svg>
  <h1 class="flyer__title">FAHRANGST <em>ERFOLGREICH</em> ÜBERWINDEN!</h1>
  <svg class="hero-photo" style="top:60px" width="394" height="290" viewBox="0 0 394 290" role="img" aria-label="Foto: gestresste Frau am Steuer eines Autos">
    <defs><linearGradient id="g1" x1="0" y1="0" x2="1" y2="1"><stop offset="0" stop-color="var(--photo-b)"/><stop offset=".6" stop-color="var(--photo-a)"/><stop offset="1" stop-color="#e9ece8"/></linearGradient></defs>
    <path d="M0 24 C120 -8 270 -8 394 15 L394 185 C240 240 120 270 0 285 Z" fill="url(#g1)"/>
  </svg>
  <div class="badge" style="left:253px;top:237px">GEHT ES<br>IHNEN AUCH<br>SO?</div>

  <div class="headline bebas" style="left:110px;top:346px;width:170px;font-size:33px">WOLLEN SIE</div>
  <ul class="wish-list" style="left:45px;top:388px">
    <li><span class="tick-dot"><svg width="7" height="6" viewBox="0 0 7 6"><path d="M1 3 L3 5 L6 1" stroke="#fff" stroke-width="1.4" fill="none"/></svg></span>Fahrangst überwinden?</li>
    <li><span class="tick-dot"><svg width="7" height="6" viewBox="0 0 7 6"><path d="M1 3 L3 5 L6 1" stroke="#fff" stroke-width="1.4" fill="none"/></svg></span>Panikattacken beim Auto fahren loswerden?</li>
    <li><span class="tick-dot"><svg width="7" height="6" viewBox="0 0 7 6"><path d="M1 3 L3 5 L6 1" stroke="#fff" stroke-width="1.4" fill="none"/></svg></span>Sicher und entspannt Autofahren?</li>
  </ul>
  <div class="pill bebas" style="left:74px;top:472px;width:245px;height:27px;font-size:17px">DANN SIND SIE HIER RICHTIG!</div>
  <div class="headline bebas" style="left:0;top:517px;width:394px;font-size:16px">KOMMT IHNEN EINE DIESER SITUATIONEN BEKANNT VOR?</div>
  <ul class="detail-list" style="left:16px;top:543px;width:362px">
    <li><span class="hl">Autofahren erleben Sie unter hoher Anspannung und Stress.</span> - Sie wünschen sich, Autofahren sicher und entspannt zu erleben.</li>
    <li><span class="hl">Bestimmte Situationen (z.B. unbekannte Strecken, Autobahnen, Baustellen, Stadtverkehr, Fahrspurwechsel, Einparken...) bereiten Ihnen großen Stress, und Sie trauen sie sich nicht (mehr) zu.</span> - Sie möchten diese Situationen gelassen und souverän meistern.</li>
    <li><span class="hl">Sie fühlen sich durch andere Verkehrsteilnehmer gestresst und unter Druck gesetzt. Sie haben Angst, auf unvorhergesehene Situationen nicht richtig zu reagieren.</span> - Sie möchten Autofahren entspannter und souveräner erleben.</li>
    <li><span class="hl">Angst oder Panikattacken begleiten Sie beim Autofahren. Vielleicht vermeiden Sie deshalb das Autofahren komplett.</span> - Sie möchten/müssen (beruflich) mobil sein und bleiben.</li>
  </ul>
  <div class="headline bebas" style="left:255px;top:707px;width:100px;font-size:21px;line-height:1">AUCH SIE<br>KÖNNEN<br>ES SCHAFFEN!!</div>
  <div class="contact" style="top:780px">
    <div class="contact__phone"><svg width="12" height="12" viewBox="0 0 24 24"><path d="M6.6 10.8a15 15 0 006.6 6.6l2.2-2.2a1 1 0 011-.25 11.4 11.4 0 003.6.57 1 1 0 011 1V20a1 1 0 01-1 1A17 17 0 013 4a1 1 0 011-1h3.5a1 1 0 011 1 11.4 11.4 0 00.57 3.6 1 1 0 01-.25 1z" fill="var(--green)"/></svg>0151 00 12 34 56</div>
    <div class="contact__web">www.fahrangst-gelassen-coach.de</div>
  </div>
</section>

<!-- Page 2 -->
<section class="flyer flyer--back">
  <svg class="flyer__bg" width="394" height="828" viewBox="0 0 394 828" aria-hidden="true">
    <rect x="0" y="230" width="394" height="560" fill="var(--panel)"/>
    <path d="M0 730 C130 700 260 770 394 740 L394 828 L0 828 Z" fill="#fff"/>
    <path d="M0 745 C100 700 200 740 280 785 C330 808 365 800 394 770 L394 790 C355 815 310 815 260 795 C180 755 100 730 0 760 Z" fill="var(--green)"/>
    <path d="M0 84 C120 50 270 50 394 75 L394 62 C270 40 120 42 0 74 Z" fill="var(--green)"/>
    <path d="M0 230 C110 210 220 270 394 230 L394 250 C230 290 110 232 0 250 Z" fill="var(--green)"/>
  </svg>
  <h1 class="flyer__title">FAHRANGST <em>ERFOLGREICH</em> ÜBERWINDEN!</h1>
  <svg class="hero-photo" style="top:60px" width="394" height="185" viewBox="0 0 394 185" role="img" aria-label="Foto: lächelnde Frau im Auto mit erhobenem Daumen">
    <defs><linearGradient id="g2" x1="0" y1="0" x2="1" y2="1"><stop offset="0" stop-color="#b7b78f"/><stop offset=".5" stop-color="#d9c6a8"/><stop offset="1" stop-color="#7f8c92"/></linearGradient></defs>
    <path d="M0 24 C120 -8 270 -8 394 15 L394 172 C220 212 110 150 0 172 Z" fill="url(#g2)"/>
  </svg>
  <div class="badge" style="left:262px;top:163px">ICH HAB'S<br>GESCHAFFT!!</div>

  <div class="headline bebas" style="left:0;top:285px;width:394px;font-size:18px">3 SCHRITTE ZUR LÖSUNG:</div>
  <div class="step" style="left:48px"><span class="step__num bebas">1.</span><span class="step__text">Erstgespräch vereinbaren</span></div>
  <div class="step" style="left:154px"><span class="step__num bebas">2.</span><span class="step__text">Analyse Ihrer individuellen Situation und Zielsetzung</span></div>
  <div class="step" style="left:259px"><span class="step__num bebas">3.</span><span class="step__text">Individuelles Coaching und Training</span></div>
  <div class="pill bebas" style="left:73px;top:400px;width:245px;height:28px;font-size:16px">IHRE VORTEILE IN DER ARBEIT MIT MIR:</div>
  <ul class="detail-list" style="left:16px;top:438px;width:362px">
    <li><span class="hl">Über 10 Jahre Erfahrung als Fahrsicherheits-Trainerin und Fahrangst-Bewältigungs-Coach:</span> Ich helfe Ihnen gezielt, Entspannungstechniken einzusetzen und Ängste und Panik beim Autofahren zu überwinden. Sie profitieren von meinen Tipps &amp; Tricks bei Unsicherheiten z.B. beim Fahrspurwechsel, Einparken, Autobahn...</li>
    <li><span class="hl">100 % auf Sie zugeschnitten:</span> Ich begleite Sie zielführend in Ihrem individuellen Prozess der Angst-/Paniküberwindung und/oder Erhöhung Ihrer Fahrsicherheit/-kompetenz.</li>
    <li>Wir <span class="hl">trainieren Schritt für Schritt -exakt auf Sie abgestimmt- in Ihrem eigenen Fahrzeug</span></li>
    <li>Wenn es Ihnen nicht möglich ist, in meine Praxis zu kommen:<br><span class="hl">Mit der „mobilen Praxis“ komme ich auch zu Ihnen.</span></li>
  </ul>
  <div class="coach-photo" role="img" aria-label="Porträtfoto der Fahrangst-Bewältigungs-Coach"></div>
  <p class="quote"><span class="quote__mark">“</span>Auch Sie können es schaffen!<br>&nbsp;&nbsp;&nbsp;Ich helfe Ihnen dabei.<span class="quote__mark">”</span></p>
  <p class="coach-name">Sabine Marlow<small>Fahrangst-Bewältigungs-Coach</small></p>
  <div class="contact" style="top:772px">
    <div class="contact__phone"><svg width="12" height="12" viewBox="0 0 24 24"><path d="M6.6 10.8a15 15 0 006.6 6.6l2.2-2.2a1 1 0 011-.25 11.4 11.4 0 003.6.57 1 1 0 011 1V20a1 1 0 01-1 1A17 17 0 013 4a1 1 0 011-1h3.5a1 1 0 011 1 11.4 11.4 0 00.57 3.6 1 1 0 01-.25 1z" fill="var(--green)"/></svg>0151 00 12 34 56</div>
    <div class="contact__web">www.fahrangst-gelassen-coach.de</div>
  </div>
</section>

</body>
</html>
```